Copper Ridge Aviation K740 crew cab truck partial wrap design

We are in Alaska we work hard play hard here. We are wanting a partial truck wrap on a K740 crew cab truck. We do not want a full wrap we would prefer a partial wrap design. The truck is the deep Marlo red with a topper. Our company colors are dark gray/silver, white, black and burnt orange.
We are in the process of rebranding and our updated logo is attached.
https://www.copperridgeaviation.example/
Planes we work on
https://media.qrnvx.example/media_kits/225570/
https://www.verdane-aircraft.example/en/downloads#pictures
Turbo prop owner or operator (pilots) Owners of Verdane, halvex, larkmoor airplanes
Aviation Mechanical

```html
<!DOCTYPE html>
<html lang="en">
<head>
<meta charset="utf-8">
<title>Copper Ridge Aviation – Truck Wrap Side Panel</title>
<link rel="stylesheet" href="https://fonts.googleapis.com/css2?family=Josefin+Sans:wght@400&family=Lato:wght@400;700&display=swap">
<style>
  :root {
    --paint-red: #8f1d38;
    --paint-red-deep: #6e1429;
    --band-black: #0d0d0d;
    --band-grey: #262626;
    --divider-red: #a51d36;
    --cloud-light: #d6d6d6;
    --cloud-mid: #8a8a8a;
    --cloud-dark: #3a3a3a;
    --ink-white: #ffffff;
    --canvas-bg: #e9ebea;
  }
  * { margin: 0; padding: 0; box-sizing: border-box; }
  html, body {
    width: 1200px; height: 581px; overflow: hidden;
    background: var(--canvas-bg);
  }
  .wrap-panel {
    position: relative;
    width: 1200px; height: 581px;
  }
  .wrap-art { position: absolute; inset: 0; }
  .contact {
    position: absolute;
    top: 252px; left: 290px;
    display: flex; align-items: center; gap: 8px;
    color: var(--ink-white);
    font-family: "Lato", sans-serif;
    font-weight: 700;
    font-size: 21px;
    letter-spacing: 0.8px;
  }
  .contact svg { width: 18px; height: 18px; }
  .website {
    position: absolute;
    top: 259px; left: 508px;
    color: var(--ink-white);
    font-family: "Lato", sans-serif;
    font-weight: 700;
    font-size: 10.5px;
    letter-spacing: 0.6px;
  }
  .brand-mark {
    position: absolute;
    top: 190px; left: 640px;
    display: flex; align-items: center; gap: 10px;
    color: var(--ink-white);
    font-family: "Josefin Sans", sans-serif;
    font-weight: 400;
    font-size: 22px;
    letter-spacing: 1.5px;
  }
  .brand-mark .dot {
    width: 46px; height: 46px; border-radius: 50%;
    background: var(--ink-white);
  }
  .company-name {
    position: absolute;
    top: 290px; left: 290px;
    color: var(--ink-white);
    font-family: "Josefin Sans", sans-serif;
    font-weight: 400;
    font-size: 38px;
    letter-spacing: 3px;
    white-space: nowrap;
  }
  .services {
    position: absolute;
    top: 346px; left: 285px;
    display: flex; align-items: center;
    list-style: none;
    color: #d9d9d9;
    font-family: "Lato", sans-serif;
    font-weight: 400;
    font-size: 9.5px;
    letter-spacing: 0.3px;
    line-height: 1;
    text-align: center;
  }
  .services li {
    padding: 0 10px;
    border-left: 2px solid var(--divider-red);
    min-height: 22px;
    display: flex; align-items: center;
  }
  .services li:first-child { border-left: none; }
  .services .service-inspections { width: 83px; }
  .services .service-balancing { width: 122px; }
  .services .service-cnc { width: 104px; }
  .services .service-scan { width: 91px; }
  .services .service-cad { width: 90px; }
</style>
</head>
<body>
<main class="wrap-panel">
  <svg class="wrap-art" viewBox="0 0 1200 581" width="1200" height="581" aria-hidden="false">
    <defs>
      <linearGradient id="band-fade" x1="0" y1="0" x2="0" y2="1">
        <stop offset="0" stop-color="var(--band-black)"/>
        <stop offset="1" stop-color="var(--band-grey)"/>
      </linearGradient>
      <radialGradient id="sky-photo" cx="0.55" cy="0.35" r="0.75">
        <stop offset="0" stop-color="var(--cloud-light)"/>
        <stop offset="0.5" stop-color="var(--cloud-mid)"/>
        <stop offset="1" stop-color="var(--cloud-dark)"/>
      </radialGradient>
    </defs>

    <!-- painted body area -->
    <path class="body-paint" d="M60 140 Q60 125 75 125 L1120 125 Q1140 125 1140 145 L1140 385 L60 385 Z" fill="var(--paint-red)"/>

    <!-- lower dark sweep -->
    <path class="lower-sweep" d="M260 385 L272 300 Q280 285 300 285 L760 285 Q780 285 795 270 L870 125 L1140 125 L1140 385 Z" fill="url(#band-fade)"/>

    <!-- jet photo area -->
    <path class="photo-area" role="img" aria-label="Black-and-white photo of a business jet flying through clouds"
          d="M870 125 L1110 125 Q1135 128 1138 160 L1140 320 L830 320 L790 285 Q790 285 800 270 Z" fill="url(#sky-photo)"/>

    <!-- white pinstripe along the sweep -->
    <path class="pinstripe" d="M262 310 Q272 287 300 286 L760 286 Q782 286 796 268 L870 125"
          fill="none" stroke="var(--ink-white)" stroke-width="1.5"/>
    <line class="band-rule" x1="278" y1="340" x2="830" y2="340" stroke="var(--ink-white)" stroke-width="1.2"/>
    <line class="band-rule" x1="1030" y1="333" x2="1120" y2="333" stroke="var(--ink-white)" stroke-width="1.2"/>
  </svg>

  <div class="contact">
    <svg viewBox="0 0 24 24" aria-hidden="true"><path fill="#ffffff" d="M6.6 10.8a15.1 15.1 0 0 0 6.6 6.6l2.2-2.2c.3-.3.7-.4 1-.2 1.1.4 2.3.6 3.6.6.6 0 1 .4 1 1V20c0 .6-.4 1-1 1A17 17 0 0 1 3 4c0-.6.4-1 1-1h3.5c.6 0 1 .4 1 1 0 1.3.2 2.5.6 3.6.1.3 0 .7-.2 1z"/></svg>
    <span class="phone">(907)555-0148</span>
  </div>
  <div class="website">copperridgeaviation.example</div>

  <div class="brand-mark">
    <span class="dot"></span>
    <span class="brand-name">Copper Ridge</span>
  </div>

  <h1 class="company-name">COPPER RIDGE AVIATION</h1>

  <ul class="services">
    <li class="service-inspections">INSPECTIONS</li>
    <li class="service-balancing">DYNAMIC PROPELLER<br>BALANCING</li>
    <li class="service-cnc">CNC MACHINING</li>
    <li class="service-scan">3D SCANNING</li>
    <li class="service-cad">CAD DESIGN &amp;<br>ENGINEERING</li>
  </ul>
</main>
</body>
</html>
```